Business Card Design Project

I need a new business card design for my building/development company: Kestrel Ridge Builders.

We specialise in small sub-divisions, multi-story developments and new house builds.
We handle the whole process from concept stage right throught to a fully developed property.
Updates

Target Market(s)

people looking to develop their property and need help. New property buyers

Industry/Entity Type

House

Requirements
Must have
• My logo on both sides:
Side 1: Logo taking up whole side as per old card but with a color/style change.

Side 2: Contact page: include logo but the rest just surprise me!

All contact details will be: (and need to be changable for each employee) I'll inform you of specifics before printing.

Name Surname
Position ie. Managing director
M: insert mobile
E: insert email
P.O. Box 518, Ashwell, Vic, 3094
www.kestrelridgebuilders.com.au

Nice to have
• Colors i'd like: (not necessarily all but this is the basic idea)

Black, blue, grey, silver, white

```html
<!DOCTYPE html>
<html lang="en">
<head>
<meta charset="utf-8">
<title>Kestrel Ridge Builders – Business Cards</title>
<link href="https://fonts.googleapis.com/css2?family=Open+Sans:wght@400;600;700&display=swap" rel="stylesheet">
<style>
  :root {
    --page-bg: #d9d9d9;
    --card-black: #050505;
    --card-glow: #3a3a3a;
    --brand-blue: #1d8fe0;
    --brand-blue-light: #5cc0ff;
    --text-white: #ffffff;
    --text-soft: #e6e6e6;
  }
  * { box-sizing: border-box; margin: 0; padding: 0; }
  html, body {
    width: 954px; height: 1200px; overflow: hidden;
    background: var(--page-bg);
    font-family: "Open Sans", Arial, sans-serif;
  }
  .canvas { position: relative; width: 954px; height: 1200px; }

  .card {
    position: absolute; left: 77px; width: 800px; height: 456px;
    border-radius: 28px; overflow: hidden;
    background: radial-gradient(ellipse 60% 65% at 50% 48%, var(--card-glow) 0%, #181818 45%, var(--card-black) 85%);
    box-shadow: 0 10px 24px rgba(0,0,0,0.35);
    color: var(--text-white); text-align: center;
  }
  .card--contact { top: 78px; }
  .card--brand { top: 634px; }

  .card__corners { position: absolute; inset: 0; width: 100%; height: 100%; }

  .brand { position: absolute; left: 0; right: 0; display: flex; justify-content: center; align-items: center; gap: 14px; }
  .brand__mark { background: var(--brand-blue); display: block; }
  .brand__name { font-weight: 600; color: var(--text-white); letter-spacing: -0.5px; white-space: nowrap; }
  .tagline { position: absolute; left: 0; right: 0; color: var(--text-soft); letter-spacing: 0.4px; }

  .card--contact .brand { top: 196px; }
  .card--contact .brand__mark { width: 26px; height: 26px; }
  .card--contact .brand__name { font-size: 40px; line-height: 56px; }
  .card--contact .tagline { top: 250px; font-size: 21px; }

  .person { position: absolute; left: 0; right: 0; top: 303px; font-size: 21px; }
  .person__role { font-size: 17px; }
  .contact { position: absolute; left: 0; right: 0; font-size: 17px; color: var(--text-soft); }
  .contact b { font-weight: 700; color: var(--text-white); }
  .contact--mobile { top: 344px; }
  .contact--email { top: 371px; }
  .contact--web { top: 397px; }

  .card--brand .brand { top: 226px; }
  .card--brand .brand__mark { width: 34px; height: 34px; }
  .card--brand .brand__name { font-size: 52px; line-height: 72px; }
  .card--brand .tagline { top: 298px; font-size: 26px; }
</style>
</head>
<body>
<main class="canvas">

  <section class="card card--contact">
    <svg class="card__corners" viewBox="0 0 800 456" aria-hidden="true">
      <defs>
        <linearGradient id="cornerBlueA" x1="0" y1="0" x2="1" y2="1">
          <stop offset="0" stop-color="var(--brand-blue-light)"/>
          <stop offset="1" stop-color="var(--brand-blue)"/>
        </linearGradient>
      </defs>
      <path d="M735 0 H800 V90 C785 50 765 20 735 0 Z" fill="url(#cornerBlueA)"/>
      <path d="M725 0 C760 18 785 50 800 95" fill="none" stroke="#000" stroke-width="6" opacity="0.6"/>
      <path d="M0 355 V456 H95 C50 440 15 405 0 355 Z" fill="url(#cornerBlueA)"/>
      <path d="M0 345 C12 400 48 440 105 456" fill="none" stroke="#000" stroke-width="6" opacity="0.6"/>
    </svg>

    <div class="brand"><span class="brand__mark"></span><span class="brand__name">Kestrel Ridge Builders</span></div>
    <p class="tagline">renovation-construction-development</p>

    <p class="person">Your Name - <span class="person__role">Managing director</span></p>
    <p class="contact contact--mobile"><b>m</b> : 0400 555 219 &nbsp;|&nbsp; P.O. Box 518, Ashwell, Vic, 3094</p>
    <p class="contact contact--email"><b>e</b> : info@kestrelridgebuilders.com.au</p>
    <p class="contact contact--web"><b>w</b> : www.kestrelridgebuilders.com.au</p>
  </section>

  <section class="card card--brand">
    <svg class="card__corners" viewBox="0 0 800 456" aria-hidden="true">
      <defs>
        <linearGradient id="cornerBlueB" x1="0" y1="0" x2="1" y2="1">
          <stop offset="0" stop-color="var(--brand-blue-light)"/>
          <stop offset="1" stop-color="var(--brand-blue)"/>
        </linearGradient>
      </defs>
      <path d="M735 0 H800 V90 C785 50 765 20 735 0 Z" fill="url(#cornerBlueB)"/>
      <path d="M725 0 C760 18 785 50 800 95" fill="none" stroke="#000" stroke-width="6" opacity="0.6"/>
      <path d="M0 355 V456 H95 C50 440 15 405 0 355 Z" fill="url(#cornerBlueB)"/>
      <path d="M0 345 C12 400 48 440 105 456" fill="none" stroke="#000" stroke-width="6" opacity="0.6"/>
    </svg>

    <div class="brand"><span class="brand__mark"></span><span class="brand__name">Kestrel Ridge Builders</span></div>
    <p class="tagline">renovation-construction-development</p>
  </section>

</main>
</body>
</html>
```